Doggy Easter Marketing Banners & design

Hi All,
We are looking to start outsourcing our Marketing Banner designs for when we have sales coming up to free up our time to run the business in other areas.

Brief –
Easter design & look for social media incorporating our products and logo.
The same designs can be used for all 4 sizes (see below) or we are open to having different designs for each size.

What we are looking for -
* Creativity
* A dog or dogs to feature in design (real life images, no cartoons)
* Products to stand out
* No busy designs. Keep it simple yet stylish.
* PawLuxe Logo
* Keeping within our website design & look (boutique & fashionable)

Wording / Text to include –
Easter Collection
Pre-order Now and Get 20% OFF
Pre-order ends 4th March 2018

Ad / Picture Sizes –
Facebook Cover Photo – 851 x 315
Facebook like ad – 1200 x 444
Instagram / Facebook post – 700 x 695
Website Banner – 1180 x 500

We will try and give feedback (positive & constructive) where possible, if the brief isn’t met, we will give it 1 or no stars.

To show your design skills, you are welcome to do 1 design for the competition or multiple ones for us judge.

You can see our products on the link below. Not all photos uploaded need to be used, but added ones that can be utilised in the design.

https://www.pawluxe-example.com.au/collections/all/easter

If you have any questions, please let us know.
Best of luck,
Colette & Rory

```html
<!DOCTYPE html>
<html lang="en">
<head>
<meta charset="utf-8">
<title>PawLuxe Easter Collection Banner</title>
<link rel="stylesheet" href="https://fonts.googleapis.com/css2?family=Russo+One&display=swap">
<style>
  :root {
    --stage: #1c1c1c;
    --paper: #ffffff;
    --ink: #111111;
    --sale-red: #e8141b;
    --easter-blue: #1a8cf0;
    --easter-outline: #0b2f66;
    --sun-yellow: #fcc10c;
    --edge-black: #0a0a0a;
    --outfit-pink: #f4cfdc;
    --outfit-blue: #cdebf2;
    --outfit-lilac: #e6e0ef;
    --outfit-grey: #e4e2e2;
    --fur-white: #f7f6f2;
  }
  * { margin: 0; padding: 0; box-sizing: border-box; }
  html, body {
    width: 1200px;
    height: 724px;
    overflow: hidden;
    background: var(--stage);
  }
  .banner {
    position: absolute;
    left: 0;
    top: 140px;
    width: 1200px;
    height: 444px;
    background: var(--paper);
    overflow: hidden;
  }
  .product-collage {
    position: absolute;
    left: 12px;
    top: 16px;
    width: 584px;
    height: 414px;
    background:
      radial-gradient(circle at 15% 20%, var(--outfit-pink) 0%, rgba(255,255,255,0) 32%),
      radial-gradient(circle at 55% 18%, var(--outfit-grey) 0%, rgba(255,255,255,0) 30%),
      radial-gradient(circle at 88% 22%, var(--outfit-pink) 0%, rgba(255,255,255,0) 28%),
      radial-gradient(circle at 18% 52%, var(--outfit-blue) 0%, rgba(255,255,255,0) 26%),
      radial-gradient(circle at 60% 52%, var(--outfit-pink) 0%, rgba(255,255,255,0) 26%),
      radial-gradient(circle at 15% 82%, var(--outfit-lilac) 0%, rgba(255,255,255,0) 28%),
      radial-gradient(circle at 50% 82%, var(--outfit-pink) 0%, rgba(255,255,255,0) 28%),
      radial-gradient(circle at 85% 80%, var(--outfit-pink) 0%, rgba(255,255,255,0) 26%),
      var(--paper);
  }
  .yellow-panel {
    position: absolute;
    left: 0;
    top: 0;
    width: 1200px;
    height: 444px;
  }
  .dog-photo {
    position: absolute;
    left: 945px;
    top: 72px;
    width: 245px;
    height: 280px;
    border-radius: 48% 52% 38% 42% / 40% 44% 56% 60%;
    background: radial-gradient(ellipse at 50% 45%, var(--fur-white) 0%, #efede7 55%, rgba(239,237,231,0) 72%);
  }
  .offer {
    position: absolute;
    left: 584px;
    top: 28px;
    width: 330px;
    text-align: center;
    font-family: "Russo One", sans-serif;
    color: var(--ink);
  }
  .brand-name {
    display: block;
    font-size: 38px;
    line-height: 52px;
    color: var(--ink);
  }
  .collection-title {
    margin-top: 36px;
    font-family: "Russo One", sans-serif;
    font-weight: 400;
    color: var(--easter-blue);
    text-transform: uppercase;
    line-height: 53px;
    text-shadow:
      2px 0 0 var(--easter-outline), -2px 0 0 var(--easter-outline),
      0 2px 0 var(--easter-outline), 0 -2px 0 var(--easter-outline),
      1.5px 1.5px 0 var(--easter-outline), -1.5px -1.5px 0 var(--easter-outline),
      1.5px -1.5px 0 var(--easter-outline), -1.5px 1.5px 0 var(--easter-outline);
  }
  .collection-title .line-one { display: block; font-size: 44px; }
  .collection-title .line-two { display: block; font-size: 46px; }
  .offer-lead {
    margin-top: 10px;
    font-size: 23px;
    line-height: 34px;
    text-transform: uppercase;
    white-space: nowrap;
  }
  .offer-discount {
    font-size: 52px;
    line-height: 60px;
    color: var(--sale-red);
  }
  .offer-deadline {
    font-size: 26px;
    line-height: 34px;
    text-transform: uppercase;
  }
  .offer-date {
    font-size: 35px;
    line-height: 50px;
    color: var(--sale-red);
    text-transform: uppercase;
    white-space: nowrap;
  }
</style>
</head>
<body>
  <section class="banner">
    <div class="product-collage" role="img" aria-label="Collage of pastel Easter dog outfits: bunny-ear hoodies, rabbit print boots and patterned dresses"></div>

    <svg class="yellow-panel" viewBox="0 0 1200 444" aria-hidden="true">
      <polygon points="1008,0 1200,0 1200,444 909,444 944,230" fill="var(--sun-yellow)"/>
      <polyline points="1008,0 944,230 909,444" fill="none" stroke="var(--edge-black)" stroke-width="11"/>
    </svg>

    <div class="dog-photo" role="img" aria-label="Photo of a white fluffy Samoyed dog standing side-on"></div>

    <div class="offer">
      <span class="brand-name">PawLuxe</span>
      <h1 class="collection-title">
        <span class="line-one">Easter</span>
        <span class="line-two">Collection</span>
      </h1>
      <p class="offer-lead">Pre-order now and get</p>
      <p class="offer-discount">20% OFF</p>
      <p class="offer-deadline">Pre-order ends</p>
      <p class="offer-date">4th March 2018</p>
    </div>
  </section>
</body>
</html>
```